Business Card and Stationery for Interior Design Company
Silver Kettle Design
Designers,
On the back of my card on want the following services listed:
Interior Decorating
Room Redesign
Space Planning
Paint Color Selection
Furnishings & Accessories
The fonts used in the logo are as follows:
fonts:
Kozuka Mincho Pr6N M
Miss Le Gatees (modified)
RT/KPF/JN Team
My tagline "Design with Vision" does NOT have to be the same font as the original logo font. Neither does my Name. In fact, tagline should probably be italic and my Name I'd like to see perhaps in a similar script font like the word INTERIOR.

```html
<!DOCTYPE html>
<html lang="en">
<head>
<meta charset="utf-8">
<title>Silver Kettle Design – Envelope</title>
<link rel="stylesheet" href="https://fonts.googleapis.com/css2?family=Cormorant+Garamond:wght@500&display=swap">
<style>
  :root {
    --backdrop: #e3e5e7;
    --paper: #ffffff;
    --paper-edge: #d6d8da;
    --fold-line: #eceeef;
    --stripe: #ebe9e6;
    --brand-ink: #8b6b4c;
    --address-ink: #7a6a5a;
    --mark-fill: #9fc7c0;
  }
  html, body {
    margin: 0;
    padding: 0;
    width: 1200px;
    height: 679px;
    overflow: hidden;
    background: var(--backdrop);
  }
  .canvas {
    display: block;
    width: 1200px;
    height: 679px;
  }
  .paper { fill: var(--paper); stroke: var(--paper-edge); stroke-width: 1; }
  .fold { stroke: var(--fold-line); stroke-width: 1; fill: none; }
  .brand-name {
    font-family: "Cormorant Garamond", serif;
    font-weight: 500;
    fill: var(--brand-ink);
  }
  .return-address {
    font-family: "Cormorant Garamond", serif;
    font-weight: 500;
    fill: var(--address-ink);
  }
  .brand-mark { fill: var(--mark-fill); }
</style>
</head>
<body>
<svg class="canvas" viewBox="0 0 1200 679" xmlns="http://www.w3.org/2000/svg">
  <defs>
    <pattern id="flap-stripes" width="16" height="16" patternUnits="userSpaceOnUse">
      <rect width="16" height="16" fill="var(--paper)"/>
      <rect width="8" height="16" fill="var(--stripe)"/>
    </pattern>
    <clipPath id="open-flap-clip">
      <path d="M290 110 L300 62 Q304 42 324 42 L536 42 Q556 42 560 62 L570 110 Z"/>
    </clipPath>
  </defs>

  <!-- Envelope dieline, unfolded -->
  <g class="envelope-dieline">
    <path class="paper" d="M290 110 L300 62 Q304 42 324 42 L536 42 Q556 42 560 62 L570 110
             L652 232 L652 330 L570 555 L432 615 L290 555 L96 340 L96 280 Z"/>
    <rect x="290" y="42" width="280" height="68" fill="url(#flap-stripes)" clip-path="url(#open-flap-clip)"/>
    <line class="fold" x1="290" y1="110" x2="570" y2="110"/>
    <line class="fold" x1="290" y1="110" x2="290" y2="555"/>
    <line class="fold" x1="570" y1="110" x2="570" y2="555"/>
    <line class="fold" x1="290" y1="412" x2="570" y2="412"/>
    <line class="fold" x1="290" y1="555" x2="570" y2="555"/>

    <g class="flap-brand" transform="rotate(180 430 76)">
      <rect class="brand-mark" x="423" y="52" width="14" height="14"/>
      <text class="return-address" x="430" y="98" font-size="8" text-anchor="middle">1480 Willow Bend Lane Dayton OH 45402</text>
    </g>

    <g class="front-brand">
      <rect class="brand-mark" x="300" y="190" width="22" height="22"/>
      <text class="brand-name" x="300" y="236" font-size="15">Silver Kettle</text>
      <text class="brand-name" x="322" y="254" font-size="15">Design</text>
    </g>
  </g>

  <!-- Envelope, folded and sealed -->
  <g class="envelope-closed">
    <rect class="paper" x="497" y="271" width="408" height="217"/>
    <path d="M497 271 L905 271 L905 302 L701 334 L497 302 Z" fill="url(#flap-stripes)"/>
    <path class="fold" d="M497 302 L701 334 L905 302" stroke="var(--paper-edge)"/>
    <rect class="brand-mark" x="695" y="282" width="12" height="12"/>
    <text class="return-address" x="701" y="313" font-size="8" text-anchor="middle">1480 Willow Bend Lane Dayton OH 45402</text>
  </g>
</svg>
</body>
</html>
```